Online medical reviews website needs banner advert!

We need banner advert templates for our website, www.traineepanel.net. These should meet the technical requirements of our partner (uploaded).

Our groundbreaking website allows doctors in training to rate and review their training.

The adverts should use the same modern design language and colour scheme as our website. They should use the text 'Help a junior doctor make a big decision - rate your training!'.

Vector assets should be supplied, allowing us to use alternative text in future.
Updates

Industry/Entity Type

Healthcare

Font styles to use
Other font styles liked:
• Karla

Colors
3277b5
0555a3
ffffff

Requirements
Must have
• Similar design to our website. Should be elegant & modern. Must allow future text to be easily inserted.
Should not have
• Unrelated design.

```html
<!DOCTYPE html>
<html lang="en">
<head>
<meta charset="utf-8">
<title>Trainee Panel – Banner Set</title>
<link href="https://fonts.googleapis.com/css2?family=Quicksand:wght@400;700&family=Roboto+Condensed:wght@700&display=swap" rel="stylesheet">
<style>
  :root {
    --navy: #13306b;
    --white: #ffffff;
    --board-light: #e2e2e2;
    --board-dark: #9a9a9a;
    --photo-light: #eef3f7;
    --photo-mid: #c9d8e6;
    --photo-warm: #c8b49a;
    --scrubs: #4f84c4;
  }
  html, body {
    margin: 0;
    width: 1200px;
    height: 1200px;
    overflow: hidden;
  }
  .board {
    position: relative;
    width: 1200px;
    height: 1200px;
    background: radial-gradient(ellipse at 50% 45%, var(--board-light) 0%, #c4c4c4 60%, var(--board-dark) 100%);
  }
  .banner {
    position: absolute;
    overflow: hidden;
    background: var(--navy);
    color: var(--white);
  }
  .banner .photo {
    position: absolute;
    left: 0; top: 0;
  }
  .banner svg.panel {
    position: absolute;
    left: 0; top: 0;
  }
  .line {
    position: absolute;
    margin: 0;
    white-space: nowrap;
    line-height: 1;
  }
  .tagline {
    font-family: "Roboto Condensed", "Arial Narrow", sans-serif;
    font-weight: 700;
    letter-spacing: 0.09em;
  }
  .headline {
    font-family: "Quicksand", "Arial Rounded MT Bold", sans-serif;
    font-weight: 700;
    letter-spacing: -0.05em;
  }
  .brand {
    font-family: "Quicksand", "Arial", sans-serif;
    font-weight: 400;
    letter-spacing: -0.03em;
  }
  .centered { left: 0; right: 0; text-align: center; }

  /* Skyscraper */
  .banner--tall { left: 145px; top: 61px; width: 448px; height: 897px; }
  .banner--tall .photo { width: 448px; height: 470px;
    background: linear-gradient(160deg, var(--photo-light) 0%, #dfe8ef 45%, var(--photo-mid) 100%); }
  .banner--tall .tagline { font-size: 33px; left: 40px; }
  .banner--tall .headline { font-size: 82px; left: 44px; }
  .banner--tall .brand { font-size: 40px; left: 40px; top: 808px; }

  /* Rectangles */
  .banner--rect-a { left: 642px; top: 76px; width: 458px; height: 380px; }
  .banner--rect-a .photo { width: 458px; height: 275px;
    background: linear-gradient(120deg, var(--photo-mid) 0%, var(--photo-light) 55%, #d7e3ea 100%); }
  .banner--rect-b { left: 642px; top: 549px; width: 456px; height: 379px; }
  .banner--rect-b .photo { width: 456px; height: 240px;
    background: linear-gradient(100deg, #dfe6ea 0%, var(--photo-warm) 55%, var(--scrubs) 100%); }
  .banner--rect .brand { font-size: 27px; }
  .banner--rect .tagline { font-size: 20px; }
  .banner--rect .headline { font-size: 47px; }

  /* Leaderboard */
  .banner--wide { left: 143px; top: 1000px; width: 960px; height: 118px; }
  .banner--wide .photo { left: auto; right: 0; width: 260px; height: 118px;
    background: linear-gradient(90deg, var(--photo-light) 0%, #f6f8fa 50%, var(--photo-mid) 100%); }
  .banner--wide .tagline { font-size: 32px; left: 27px; }
  .banner--wide .headline { font-size: 45px; left: 374px; top: 28px; }
  .banner--wide .brand { font-size: 24px; left: 502px; top: 78px; }
</style>
</head>
<body>
<main class="board">

  <!-- Skyscraper -->
  <section class="banner banner--tall">
    <div class="photo" role="img" aria-label="Photo of three junior doctors in white coats with stethoscopes and clipboards"></div>
    <svg class="panel" width="448" height="897" viewBox="0 0 448 897" aria-hidden="true">
      <path d="M0 467 Q224 330 448 467 L448 897 L0 897 Z" fill="var(--navy)"/>
    </svg>
    <p class="line tagline" style="top:492px">Help a junior doctor</p>
    <p class="line tagline" style="top:532px">make a big decision</p>
    <p class="line headline" style="top:570px">Rate Your</p>
    <p class="line headline" style="top:652px">Training!</p>
    <p class="line brand">Trainee Panel</p>
  </section>

  <!-- Rectangle A -->
  <section class="banner banner--rect banner--rect-a">
    <div class="photo" role="img" aria-label="Photo of a senior doctor teaching a group of trainees with an anatomical heart model"></div>
    <svg class="panel" width="458" height="380" viewBox="0 0 458 380" aria-hidden="true">
      <path d="M0 268 Q229 133 458 268 L458 380 L0 380 Z" fill="var(--navy)"/>
    </svg>
    <p class="line brand centered" style="top:234px">Trainee Panel</p>
    <p class="line tagline centered" style="top:281px">Help a junior doctor make a big decision</p>
    <p class="line headline centered" style="top:308px">Rate Your Training!</p>
  </section>

  <!-- Rectangle B -->
  <section class="banner banner--rect banner--rect-b">
    <div class="photo" role="img" aria-label="Photo of a group of junior doctors in blue scrubs walking down a hospital corridor"></div>
    <svg class="panel" width="456" height="379" viewBox="0 0 456 379" aria-hidden="true">
      <path d="M0 235 Q228 115 456 235 L456 379 L0 379 Z" fill="var(--navy)"/>
    </svg>
    <p class="line brand centered" style="top:221px">Trainee Panel</p>
    <p class="line tagline centered" style="top:272px">Help a junior doctor make a big decision</p>
    <p class="line headline centered" style="top:300px">Rate Your Training!</p>
  </section>

  <!-- Leaderboard -->
  <section class="banner banner--wide">
    <div class="photo" role="img" aria-label="Photo of cheerful doctors giving a thumbs up"></div>
    <svg class="panel" width="960" height="118" viewBox="0 0 960 118" aria-hidden="true">
      <path d="M0 0 L733 0 Q800 55 745 118 L0 118 Z" fill="var(--navy)"/>
    </svg>
    <p class="line tagline" style="top:27px">Help a junior doctor</p>
    <p class="line tagline" style="top:61px">make a big decision</p>
    <p class="line headline">Rate Your Training!</p>
    <p class="line brand">Trainee Panel</p>
  </section>

</main>
</body>
</html>
```